2 page flyer for a turf supply company. MERIDELL TURF SOLUTIONS

Design a marketing flyer to be distributed to landscaping contractors, councils, and private users.
I have attached a FileCrate link that holds the logo files, copy, and brand guidelines and images.
I am wanting the brochure to be 2 pages, which can be sent as a pdf or printed double-sided. I would like a modern, professional look using the colours from the brand guidelines. We are designing a new website so this brochure will be found on the website as well as sent to clients. I have uploaded the copy, a logo, and brand guidelines. The link to more photos and logos are found on the FileCrate link below.
https://www.filecrate-share.example/scl/fo/qwk83zmtlpdnv5b2hxcrt/h?rlkey=914vbnkstpqwe7yz2mcx8lf4d&dl=0
Here is the link to the current website. https://meridellgroup.com.au/
New one coming.

Target Market(s)

The decision makers at councils, landscape businesses and land developers

Industry/Entity Type

landscaping companies and councils

Font styles to use
Sans Serif

Requirements
Must have
• must be eye catching and easy to read
Nice to have
• Bold headings

```html
<!DOCTYPE html>
<html lang="en">
<head>
<meta charset="utf-8">
<title>Meridell Turf Solutions – Flyer</title>
<link rel="stylesheet" href="https://fonts.googleapis.com/css2?family=Libre+Baskerville:wght@400;700&display=swap">
<style>
  :root {
    --brand-blue: #1c5577;
    --ink: #1a1a1a;
    --paper: #ffffff;
    --photo-green: #6f8f4e;
    --photo-sky: #a9c3d6;
    --photo-earth: #8a7a63;
  }
  * { margin: 0; padding: 0; box-sizing: border-box; }
  html, body { width: 848px; height: 1200px; overflow: hidden; background: var(--paper); }
  .flyer {
    position: relative; width: 848px; height: 1200px;
    font-family: "Libre Baskerville", Georgia, serif;
    color: var(--ink); background: var(--paper);
  }
  .hero-band {
    position: absolute; left: 0; top: 0; width: 848px; height: 748px;
    background: var(--brand-blue); color: #fff;
  }
  .footer-band {
    position: absolute; left: 0; top: 1161px; width: 848px; height: 39px;
    background: var(--brand-blue);
  }
  .block { position: absolute; left: 49px; width: 758px; }
  .headline {
    top: 52px; font-size: 19.5px; font-weight: 400; line-height: 25px;
    letter-spacing: 0.3px; text-transform: uppercase;
  }
  .body-copy { font-size: 13.3px; line-height: 22px; }
  .lede-one { top: 131px; }
  .lede-two { top: 163px; width: 520px; }
  .feature-title { font-size: 17px; font-weight: 700; }
  .premium { top: 212px; }
  .advantage { top: 340px; }
  .dedication { top: 521px; }
  .tailored { top: 606px; }
  .versatility { top: 770px; }
  .expertise { top: 881px; }
  .photo-row {
    position: absolute; top: 1009px; left: 40px; width: 770px; height: 124px;
    display: flex; justify-content: space-between;
  }
  .photo { width: 182px; height: 124px; }
  .photo-truck { background: linear-gradient(180deg, var(--photo-sky) 0%, #5b6d7e 55%, var(--photo-earth) 100%); }
  .photo-office { background: linear-gradient(180deg, #b7cde0 0%, #5f7d52 60%, #4c5e45 100%); }
  .photo-irrigation { background: linear-gradient(180deg, #c2d3e2 0%, #557a3e 45%, var(--photo-green) 100%); }
  .photo-field { background: linear-gradient(180deg, #cddbe7 0%, #4f6e45 50%, #7fa65a 100%); }
</style>
</head>
<body>
<div class="flyer">
  <section class="hero-band">
    <h1 class="block headline">Discover the green difference with<br>Meridell Turf Solutions</h1>
    <p class="block body-copy lede-one">Welcome to Meridell Turf Solutions (MTS) – your gateway to a vibrant, green landscape!</p>
    <p class="block body-copy lede-two">With over two decades of expertise in the turf industry, we are your trusted partner for superior turf solutions.</p>
    <p class="block body-copy premium"><span class="feature-title">Premium Turf Products Across NSW:</span> Over the years, our commitment to excellence has propelled us to supply premium turf products across New South Wales. Our diverse clientele includes professional sporting fields, Council parks, housing estate playing fields, public parks and gardens, as well as domestic gardens and landscaping projects.</p>
    <p class="block body-copy advantage"><span class="feature-title">The Meridell Advantage:</span> What sets our turf apart is its origin – meticulously grown in the rich alluvial soils of the fertile Richmond Lowlands, ensuring the cultivation of top-tier turf characterised by quality, resilience, and durability. Spanning approximately 300 acres along the Hawkesbury River, Meridell Turf Solutions boasts one of the largest turf farm land owners in the district. Our expansive land, coupled with full irrigation capabilities, positions MTS as a reliable source of drought-resistant turf supplies.</p>
    <p class="block body-copy dedication"><span class="feature-title">Dedication to Excellence:</span> At Meridell Turf Solutions, we are dedicated to providing the highest standard of turf for a wide range of applications. Our commitment goes beyond delivering turf – it's about transforming spaces into green havens that stand the test of time.</p>
    <p class="block body-copy tailored"><span class="feature-title">Tailored Solutions for Every Space:</span> Meridell Turf Solutions offers a range of turf varieties. Our commitment to quality extends to providing thick-cut turf, available in convenient maxi rolls or standard turf rolls. No matter the size of your project, we've got the perfect solution to bring your vision to life.</p>
  </section>

  <p class="block body-copy versatility"><span class="feature-title">Versatility with Contract Growing:</span> Need a specialised turf solution tailored to your unique specifications? Our contract growing services ensure that you get precisely what you order. We work closely with our clients, offering customized growing solutions to meet specific requirements, ensuring a seamless integration with your landscaping plans.</p>
  <p class="block body-copy expertise"><span class="feature-title">Unmatched Quality and Expertise:</span> At Meridell Turf Solutions, we don't just provide turf – we deliver a promise of quality, resilience, and expertise. Our team is dedicated to ensuring your satisfaction, from the initial consultation to the delivery of the perfect turf for your space – contact us today and experience the Meridell Advantage!</p>

  <div class="photo-row">
    <div class="photo photo-truck" role="img" aria-label="Photo of a delivery truck loaded with turf rolls"></div>
    <div class="photo photo-office" role="img" aria-label="Photo of the turf farm office building with garden"></div>
    <div class="photo photo-irrigation" role="img" aria-label="Photo of an irrigation reel on a turf field"></div>
    <div class="photo photo-field" role="img" aria-label="Photo of a green sports field with a pavilion"></div>
  </div>

  <div class="footer-band"></div>
</div>
</body>
</html>
```